New letter head for Air Conditioning business

We need a new professional letter head design to suit our new re-branded air conditioning business. Our new logo is attached

```html
<!DOCTYPE html>
<html lang="en">
<head>
<meta charset="utf-8">
<title>Norvane Letterhead</title>
<link rel="stylesheet" href="https://fonts.googleapis.com/css2?family=Figtree:wght@400;500;600;700&family=Heebo:wght@500&display=swap">
<style>
  :root {
    --backdrop: #dedede;
    --paper: #ffffff;
    --brand-green: #67c186;
    --brand-red: #ef6a5d;
    --ink: #1f1f1f;
    --ink-dark: #3b3b3d;
  }
  * { box-sizing: border-box; margin: 0; padding: 0; }
  html, body {
    width: 1200px;
    height: 800px;
    overflow: hidden;
    background: var(--backdrop);
  }
  .canvas {
    position: relative;
    width: 1200px;
    height: 800px;
  }
  .letterhead {
    position: absolute;
    left: 326px;
    top: 20px;
    width: 548px;
    height: 760px;
    background: var(--paper);
    overflow: hidden;
    font-family: "Figtree", "Helvetica Neue", Arial, sans-serif;
    color: var(--ink);
  }
  .brand {
    position: absolute;
    top: 40px;
    left: 0;
    width: 100%;
    display: flex;
    justify-content: center;
    align-items: center;
    gap: 12px;
  }
  .brand-dot {
    width: 30px;
    height: 30px;
    border-radius: 50%;
    background: var(--brand-green);
  }
  .brand-name {
    font-size: 32px;
    font-weight: 700;
    letter-spacing: 4px;
    color: var(--ink-dark);
    text-transform: uppercase;
  }
  .recipient {
    position: absolute;
    top: 206px;
    left: 28px;
    font-family: "Heebo", Arial, sans-serif;
    font-weight: 500;
    font-size: 17.5px;
    color: var(--brand-green);
  }
  .letter-body {
    position: absolute;
    top: 258px;
    left: 28px;
    right: 27px;
    font-size: 10.6px;
    line-height: 14.5px;
    letter-spacing: 0.35px;
    text-align: justify;
  }
  .letter-body p + p { margin-top: 14.5px; }
  .letter-body p.joined { margin-top: 0; }
  .closing {
    position: absolute;
    top: 538px;
    left: 28px;
    font-size: 10.6px;
    letter-spacing: 0.2px;
  }
  .footer-band {
    position: absolute;
    left: 0;
    bottom: 0;
    width: 100%;
    height: 80px;
    background: linear-gradient(to bottom, var(--brand-red) 0%, var(--brand-green) 45%, var(--brand-green) 100%);
  }
</style>
</head>
<body>
<div class="canvas">
  <article class="letterhead">
    <header class="brand">
      <span class="brand-dot"></span>
      <span class="brand-name">Norvane</span>
    </header>

    <h1 class="recipient">Daniel Hart</h1>

    <section class="letter-body">
      <p>Lorem ipsum dolor sit amet, consectetur adipiscing sed do eiusmod tempor incididunt labore et dolore magna aliqua. Ut enim ad minim veniam, quis nostrud exercitation ullamco laboris nisi ut aliquip ex ea commodo consequat.</p>
      <p>Lorem ipsum dolor sit amet, consectetur adipiscing sed do eiusmod tempor incididunt labore et dolore magna aliqua. Ut enim ad minim veniam, quis nostrud exercitation ullamco laboris nisi ut aliquip ex ea commodo consequat. Duis aute irure dolor in reprehenderit in voluptate velit esse cillum</p>
      <p class="joined">Lorem ipsum dolor sit amet, consectetur adipiscing sed do eiusmod tempor incididunt labore et dolore magna aliqua. consequat. Duis aute irure dolor in reprehenderit in voluptate velit esse cillum dolore eu fugiat nulla pariatur. Excepteur sint occaecat cupidatat non proident, sunt in culpa qui officia deserunt mollit,</p>
      <p>Lorem ipsum dolor sit amet, consectetur adipiscing sed do eiusmod tempor incididunt labore et dolore magna aliqua. Ut enim</p>
    </section>

    <p class="closing">Sincerely Yours</p>

    <div class="footer-band" role="img" aria-label="Decorative footer artwork in the brand red and green"></div>
  </article>
</div>
</body>
</html>
```